KALO Wave Co.
KALO Wave Co. - Sports
Creative Brief
Sports
www.kalowave.example
Inspired by Neptune, Roman God of the Sea, KALO Wave Co was created to produce the most cutting-edge performance and high quality boards EVER made, period.
With that being said, not everyone is meant to ride a KALO.
KALO Wave Co is a small company created by a group of close friends that LOVE the ocean, especially surfing. Our passion is in our work, and it shows in our ideas.
We want to portray the lifestyle of a true surfer: strapping their board on top of their jalopy, setting out for the unexplored coastline, and finding THE spot of their own.
Likes: Background dark in color (Feel of sunset over ocean) soft white writing. Image of surfer popping off wake on board Image of surfers *male and female having a good time (smiling, etc.) Dislike: Cookie-cutter templates
Black
Sunset Orange
Soft White
top
http://www.brimtrek.example/shop/us/en/ (background image)
http://www.dashfen.example/#/women/americacanada/teamriders/r.surf|marla_quenby (feel)
http://www.glowtrove.example/images/Waterfront%20at%20Night.jpg (photo lighting)
Edgy Cool Sexy Energy Tabs across top to include: Products, Technology, About Us, What's New, Contact Us Need good balance. Similar point of view of Tidelark/Brackenfoam/Gumbaroo Possible quote in small font "Life's too short to be ordinary" Would like to add small social network icons on lower right.

```html
<!DOCTYPE html>
<html lang="en">
<head>
<meta charset="utf-8">
<title>KALO Wave Co.</title>
<link href="https://fonts.googleapis.com/css2?family=Arimo:wght@400;700&family=Permanent+Marker&display=swap" rel="stylesheet">
<style>
  :root {
    --black: #0b0b0b;
    --charcoal: #2a2a2a;
    --steel: #5e5e5e;
    --mist: #d4d4d4;
    --mist-light: #e6e6e6;
    --soft-white: #f4f2ee;
    --sunset: #f29a1e;
    --sunset-deep: #b5560c;
    --ink: #2b2b2b;
    --muted: #555;
  }
  * { margin: 0; padding: 0; box-sizing: border-box; }
  html, body { width: 1200px; height: 1099px; overflow: hidden; }
  body {
    position: relative;
    font-family: "Arimo", Arial, sans-serif;
    color: var(--ink);
    background:
      radial-gradient(ellipse 60% 40% at 18% 8%, #8a8a8a 0%, transparent 70%),
      linear-gradient(180deg, #1c1c1c 0px, #4a4a4a 160px, var(--mist) 420px, var(--mist-light) 640px, var(--mist) 870px, var(--black) 890px, #1a1a1a 1099px);
  }
  .sea-band {
    position: absolute; left: 0; top: 880px; width: 1200px; height: 219px;
    background:
      radial-gradient(ellipse 70% 60% at 60% 30%, #3a3a3a 0%, transparent 70%),
      linear-gradient(180deg, #141414, #050505);
  }
  .brand {
    position: absolute; left: 122px; top: 78px;
    display: flex; align-items: center; gap: 14px;
  }
  .brand-name {
    font-weight: 700; font-size: 84px; line-height: 1; letter-spacing: 2px;
    color: var(--soft-white);
  }
  .brand-mark {
    width: 72px; height: 72px; border-radius: 50%;
    background: var(--sunset);
  }
  .brand-sub {
    position: absolute; left: 124px; top: 166px;
    font-size: 22px; color: var(--soft-white);
  }
  .main-nav {
    position: absolute; left: 447px; top: 143px; width: 670px; height: 65px;
    background: var(--black);
    display: flex; align-items: center; padding-left: 36px; gap: 42px;
  }
  .main-nav a {
    font-size: 15px; color: var(--soft-white); text-decoration: none;
    letter-spacing: 0.5px; text-transform: uppercase; position: relative;
  }
  .main-nav a.is-active { color: var(--sunset); }
  .main-nav a.is-active::after {
    content: ""; position: absolute; left: 0; right: 0; bottom: -10px;
    height: 2px; background: var(--sunset);
  }
  .hero {
    position: absolute; left: 106px; top: 240px; width: 1008px; height: 351px;
    border: 4px solid #1a1a1a; border-radius: 10px; overflow: hidden;
    background:
      radial-gradient(ellipse 45% 55% at 62% 45%, #f3b75a 0%, #c36d1e 40%, transparent 75%),
      linear-gradient(180deg, #6a3c14 0%, #2b1a0c 55%, #0f0a06 100%);
    box-shadow: 0 4px 12px rgba(0,0,0,0.35);
  }
  .about { position: absolute; left: 104px; top: 622px; width: 440px; }
  .section-title {
    font-size: 30px; font-weight: 400; color: var(--ink);
    padding-bottom: 10px; border-bottom: 1px solid #a9a9a9;
  }
  .about p { font-size: 15px; line-height: 24px; color: var(--muted); margin-top: 14px; }
  .about p + p { margin-top: 18px; }
  .divider {
    position: absolute; left: 566px; top: 625px; width: 1px; height: 230px;
    background: #a0a0a0;
  }
  .products { position: absolute; left: 620px; top: 622px; width: 495px; }
  .carousel {
    position: relative; margin-top: 12px; height: 100px;
    display: flex; align-items: center; gap: 6px; padding-left: 8px;
  }
  .carousel-arrow {
    position: absolute; top: 36px; width: 26px; height: 26px; border-radius: 50%;
    background: var(--black); display: flex; align-items: center; justify-content: center;
  }
  .carousel-arrow.prev { left: -30px; }
  .carousel-arrow.next { right: -16px; }
  .thumb {
    width: 74px; height: 92px; border: 2px solid #fff;
    box-shadow: 0 1px 3px rgba(0,0,0,0.4);
  }
  .thumb.t1 { background: linear-gradient(180deg, #6f8a70, #2f4a3a); }
  .thumb.t2 { background: linear-gradient(180deg, #9fc7e0, #2e6f97); }
  .thumb.t3 { background: linear-gradient(180deg, #d9d9d9, #6c6c6c); }
  .thumb.t4 { background: linear-gradient(180deg, #e9f2f8, #4d88b9); }
  .thumb.t5 { background: linear-gradient(180deg, #f7b04a, #d9561a); }
  .thumb.t6 { background: linear-gradient(180deg, #e6d6b6, #9b8455); }
  .products p { font-size: 15px; color: var(--muted); margin-top: 10px; }
  .see-more {
    display: inline-block; margin-top: 10px; font-size: 15px; font-weight: 700;
    color: var(--ink); text-decoration: none;
  }
  .faint-mark {
    position: absolute; left: 900px; top: 630px; width: 280px; height: 280px;
    border-radius: 50%; background: rgba(242,154,30,0.12);
  }
  .tagline {
    position: absolute; left: 110px; top: 918px;
    font-family: "Permanent Marker", cursive; font-size: 30px;
    color: var(--soft-white); letter-spacing: 1px; text-transform: uppercase;
  }
  .social {
    position: absolute; left: 878px; top: 918px; display: flex; gap: 12px;
  }
  .social span {
    width: 44px; height: 40px; border-radius: 6px;
    background: linear-gradient(180deg, #8a8a8a, #4c4c4c);
  }
</style>
</head>
<body>
  <div class="sea-band" role="img" aria-label="Dark ocean water surface"></div>

  <header>
    <div class="brand">
      <span class="brand-name">KALO</span>
      <span class="brand-mark"></span>
    </div>
    <div class="brand-sub">Wave Co.</div>
    <nav class="main-nav">
      <a href="#" class="is-active">Products</a>
      <a href="#">Technology</a>
      <a href="#">About Us</a>
      <a href="#">What's New</a>
      <a href="#">Contact Us</a>
    </nav>
  </header>

  <div class="hero" role="img" aria-label="Silhouettes of a male and female surfer holding boards on the beach at sunset"></div>

  <div class="faint-mark"></div>

  <section class="about">
    <h2 class="section-title">Who we are</h2>
    <p>KALO Wave Co is a small company created by a group of close friends that LOVE the ocean, especially surfing. Our passion is in our work, and it shows in our ideas.</p>
    <p>"Strap your board to your ride, set out for unexplored coast-line, and find THE spot of your own.</p>
  </section>

  <div class="divider"></div>

  <section class="products">
    <h2 class="section-title">Summer 2011 Products</h2>
    <div class="carousel">
      <span class="carousel-arrow prev">
        <svg width="10" height="12" viewBox="0 0 10 12"><path d="M8 1 L2 6 L8 11 Z" fill="#fff"/></svg>
      </span>
      <div class="thumb t1" role="img" aria-label="Product photo: surfboard outdoors"></div>
      <div class="thumb t2" role="img" aria-label="Product photo: surfer riding a wave"></div>
      <div class="thumb t3" role="img" aria-label="Product photo: surfer carrying a board"></div>
      <div class="thumb t4" role="img" aria-label="Product photo: surfer catching air"></div>
      <div class="thumb t5" role="img" aria-label="Product photo: orange surfboards"></div>
      <div class="thumb t6" role="img" aria-label="Product photo: board on sand"></div>
      <span class="carousel-arrow next">
        <svg width="10" height="12" viewBox="0 0 10 12"><path d="M2 1 L8 6 L2 11 Z" fill="#fff"/></svg>
      </span>
    </div>
    <p>Our passion is in our work, and it shows in our ideas.</p>
    <a href="#" class="see-more">See More</a>
  </section>

  <footer>
    <div class="tagline">Life's too short to be ordinary</div>
    <div class="social">
      <span></span><span></span><span></span><span></span>
    </div>
  </footer>
</body>
</html>
```